Corwith Lodge website redesign

After 8 years of our current site, we're ready to upgrade our site design. We'd like to generally make it more modern and clean and build it on a CMS like joomla for easier future maintenance.

Our hotel is a family-owned bed and breakfast that competes against much larger hotel chains in Aspen with fancier rooms and larger pricetags. Our hotel is priced moderately and features tasteful, uniquely-design rooms.

We are looking for a website that will showcase the uniqueness of our rooms, the history of the Lodge, and the friendliness of our staff.

Here are some other hotel sites we like:

http://www.brackenfoldhouse.example/

http://www.tollerpeakhaus.example/

http://www.quarrowstay.example/

*********

Scope of Work - I'm looking for a design AND build. The website should be built out in Joomla as part of the final deliverable.
Updates

Current website: http://www.corwithlodge.example/

Explanation of what design + build means:

I am looking for not only the design of the site, but also for the homepage and one subpage to be built out as well. I do NOT need the entire site built - only for those two pages to be built and I will retrofit the remainder of the pages.

Target Market(s)

travellers evaluating hotels in Aspen, Colorado.

Industry/Entity Type

Hotel

Requirements
Must have
• Must, must, must be based on a joomla template. "Rotating" large main image as central position on homepage is a must (see example websites mentioned above).

Nice to have
• We have an existing online reservation system. It would be nice to evaluate placing a "widget" on the homepage that integrates to the online reservation page. Similar to that feature that the Bracken Fold website has at the foot of the main image on their homepage.

```html
<!DOCTYPE html>
<html lang="en">
<head>
<meta charset="utf-8">
<title>Corwith Lodge</title>
<link href="https://fonts.googleapis.com/css2?family=Open+Sans:wght@400;600&family=Russo+One&family=Days+One&display=swap" rel="stylesheet">
<style>
  :root {
    --page-bg: #1e1e1e;
    --nav-top: #3b3b3b;
    --nav-bottom: #262626;
    --nav-text: #a8a8a8;
    --rust: #9c4330;
    --rust-light: #b8533a;
    --panel: #363636;
    --panel-dark: #252525;
    --olive: #a59c00;
    --olive-dark: #7d7600;
    --ribbon-edge: #8a3f18;
    --ink: #111111;
    --text: #e8e8e8;
    --muted: #bdbdbd;
    --field: #6b6b6b;
    --side-box: #5c5c5c;
    --rule: #5a5a5a;
  }
  * { box-sizing: border-box; margin: 0; padding: 0; }
  html, body { width: 1200px; height: 900px; overflow: hidden; }
  body {
    position: relative;
    background: var(--page-bg);
    font-family: "Open Sans", Arial, sans-serif;
    color: var(--text);
  }

  .main-nav {
    position: absolute; left: 0; top: 24px; width: 1200px; height: 40px;
    background: linear-gradient(var(--nav-top), var(--nav-bottom));
    display: flex; justify-content: space-between; align-items: center;
    padding: 0 48px;
  }
  .main-nav a {
    color: var(--nav-text); text-decoration: none; font-size: 13px;
    padding: 7px 20px; border-radius: 8px;
  }
  .main-nav a.is-active { background: var(--rust); color: #f3e6e0; }

  .site-panel {
    position: absolute; left: 18px; top: 78px; width: 1162px; height: 778px;
    background:
      repeating-linear-gradient(45deg, rgba(255,255,255,0.02) 0 2px, transparent 2px 4px),
      var(--panel);
    overflow: hidden;
  }

  .hero { position: absolute; left: 0; top: 0; width: 1162px; height: 470px; }
  .hero svg { position: absolute; left: 0; top: 0; display: block; }

  .brand-plate {
    position: absolute; left: 1px; top: 112px; width: 263px; height: 66px;
    background: var(--rust); display: flex; align-items: center; justify-content: center;
    font-family: "Open Sans", Arial, sans-serif; font-weight: 600; font-size: 26px; color: #ffffff;
  }

  .toll-free {
    position: absolute; left: 124px; top: 374px;
    font-family: "Russo One", sans-serif; font-size: 26px; line-height: 30px; color: var(--ink);
  }
  .hero-email {
    position: absolute; left: 143px; top: 428px;
    font-family: "Russo One", sans-serif; font-size: 14px; line-height: 18px; color: var(--ink);
  }

  .booking { position: absolute; left: 771px; top: 347px; width: 355px; }
  .booking h2 {
    font-family: "Days One", sans-serif; font-weight: 400; font-size: 14px; color: #d8d8d8;
    padding-bottom: 4px; border-bottom: 1px solid var(--rule);
  }
  .booking-fields {
    display: flex; align-items: flex-end; margin-top: 12px; padding-bottom: 22px;
    border-bottom: 1px solid var(--rule);
  }
  .field { width: 114px; margin-right: 37px; }
  .field label { display: block; font-size: 12px; color: #d0d0d0; margin-bottom: 5px; }
  .date-box {
    height: 24px; background: var(--field); display: flex; align-items: center; justify-content: space-between;
    padding: 0 4px 0 6px; font-size: 10px; color: #c4c4c4;
  }
  .go-button {
    width: 57px; height: 31px; border-radius: 10px; margin-left: -4px; margin-bottom: -2px;
    background: linear-gradient(var(--rust-light), var(--rust));
    color: #fff; font-family: "Days One", sans-serif; font-size: 14px;
    display: flex; align-items: center; justify-content: center;
  }

  .side-tab {
    position: absolute; left: 24px; top: 470px; width: 67px; height: 264px;
    background: var(--side-box); display: flex; align-items: center; justify-content: center;
  }
  .side-tab span {
    transform: rotate(-90deg); white-space: nowrap;
    font-family: "Open Sans", Arial, sans-serif; font-weight: 600; font-size: 26px; color: #ffffff;
  }

  .welcome { position: absolute; left: 126px; top: 498px; width: 710px; }
  .welcome h1 {
    font-family: "Days One", sans-serif; font-weight: 400; font-style: italic; font-size: 22px; line-height: 28px; color: #f2f2f2;
    width: 354px; border-bottom: 1px solid var(--rule); padding-left: 8px;
  }
  .welcome p { font-size: 11.5px; line-height: 13.5px; margin: 13px 0 0 10px; width: 690px; color: var(--text); }
  .welcome p.lead { margin-top: 24px; }
  .welcome p.block-start { margin-top: 27px; margin-left: 12px; }
  .welcome h1 .initial { color: #c9bd16; }

  .gallery { position: absolute; left: 876px; top: 499px; }
  .gallery h2 {
    font-family: "Days One", sans-serif; font-weight: 400; font-style: italic; font-size: 16px; line-height: 20px; color: #f2f2f2;
    margin-left: 7px;
  }
  .gallery-frame {
    margin-top: 4px; width: 257px; height: 226px; border-radius: 14px; background: var(--panel-dark);
    display: grid; grid-template-columns: 98px 98px; grid-template-rows: 78px 78px;
    column-gap: 17px; row-gap: 18px; padding: 27px 0 0 23px;
  }
  .thumb { width: 98px; height: 78px; border: 2px solid #e6e6e6; }
  .thumb-bed { background: linear-gradient(135deg, #6f5a4a, #a77c6a 50%, #4b3a30); }
  .thumb-room { background: linear-gradient(135deg, #8a4a24, #c6865a 55%, #5a3018); }

  .site-footer {
    position: absolute; left: 0; top: 856px; width: 1200px; height: 44px;
    text-align: center; font-size: 11px; color: var(--muted); line-height: 44px;
  }
  .social-badge {
    position: absolute; left: 1068px; top: 862px; width: 110px; height: 32px;
    background: #4a4a4a; border: 1px solid #5c5c5c; display: flex; align-items: center;
    padding-left: 6px; gap: 6px; text-decoration: none;
  }
  .social-badge .mark { width: 20px; height: 20px; background: #dcdcdc; }
  .social-badge .label { font-size: 10px; line-height: 11px; color: #f0f0f0; font-weight: 600; }
</style>
</head>
<body>
  <nav class="main-nav">
    <a href="#">About the Lodge</a>
    <a href="#">Rooms</a>
    <a href="#">Reservation</a>
    <a href="#" class="is-active">Amenities</a>
    <a href="#">Aspen Information</a>
    <a href="#">Manager's Journal</a>
    <a href="#">Webcams</a>
    <a href="#">Contact Us</a>
  </nav>

  <main class="site-panel">
    <section class="hero">
      <svg width="1162" height="470" viewBox="0 0 1162 470">
        <defs>
          <linearGradient id="heroTone" x1="0" y1="0" x2="1" y2="1">
            <stop offset="0" stop-color="#5a3a2a"/>
            <stop offset="0.45" stop-color="#8c6a52"/>
            <stop offset="0.75" stop-color="#6b4a36"/>
            <stop offset="1" stop-color="#3e2a20"/>
          </linearGradient>
          <linearGradient id="bandTone" x1="0" y1="0" x2="0" y2="1">
            <stop offset="0" stop-color="#b3a900"/>
            <stop offset="1" stop-color="#948c00"/>
          </linearGradient>
        </defs>
        <path role="img" aria-label="Lodge entrance at dusk in winter with stone pillars, lanterns and snow-covered shrubs"
              d="M0 0 H1162 V322 C1000 300 850 286 700 293 C560 300 450 352 300 348 C200 345 100 320 0 295 Z" fill="url(#heroTone)"/>
        <path d="M102 322 C170 338 230 347 300 348 C450 352 560 300 700 293 C850 286 1000 300 1162 322 V338 C1000 316 850 304 700 312 C600 318 520 352 472 401 L107 420 Z" fill="url(#bandTone)"/>
        <path d="M107 420 L472 401 L441 448 C340 455 230 458 133 458 Z" fill="var(--olive-dark)"/>
        <path d="M133 458 C230 458 340 455 441 448 L437 455 C340 463 230 466 136 465 Z" fill="#d8d8d8"/>
        <path d="M0 295 C100 320 200 345 300 348 C450 352 560 300 700 293 C850 286 1000 300 1162 322" fill="none" stroke="var(--ribbon-edge)" stroke-width="6"/>
      </svg>
      <div class="brand-plate">Corwith Lodge</div>
      <div class="toll-free">Toll Free : 877-555-0148</div>
      <div class="hero-email">info@corwithlodge.example</div>
    </section>

    <form class="booking">
      <h2>Best Rate Guarantee.</h2>
      <div class="booking-fields">
        <div class="field">
          <label>Arrival</label>
          <div class="date-box">MM/DD/YY
            <svg width="18" height="17" viewBox="0 0 18 17" aria-hidden="true"><rect x="1" y="2" width="16" height="14" fill="#f2f2f2"/><rect x="1" y="2" width="16" height="4" fill="#c0392b"/><g fill="#c0392b"><rect x="4" y="8" width="2" height="2"/><rect x="8" y="8" width="2" height="2"/><rect x="12" y="8" width="2" height="2"/><rect x="4" y="12" width="2" height="2"/><rect x="8" y="12" width="2" height="2"/></g></svg>
          </div>
        </div>
        <div class="field">
          <label>Departure</label>
          <div class="date-box">MM/DD/YY
            <svg width="18" height="17" viewBox="0 0 18 17" aria-hidden="true"><rect x="1" y="2" width="16" height="14" fill="#f2f2f2"/><rect x="1" y="2" width="16" height="4" fill="#c0392b"/><g fill="#c0392b"><rect x="4" y="8" width="2" height="2"/><rect x="8" y="8" width="2" height="2"/><rect x="12" y="8" width="2" height="2"/><rect x="4" y="12" width="2" height="2"/><rect x="8" y="12" width="2" height="2"/></g></svg>
          </div>
        </div>
        <div class="go-button">Go</div>
      </div>
    </form>

    <div class="side-tab"><span>Corwith Lodge</span></div>

    <section class="welcome">
      <h1><span class="initial">W</span>elcome ...</h1>
      <p class="lead">Located in the heart of downtown Aspen, the newly renovated Corwith Lodge possesses all the charms of a vintage European Ski Lodge, while offering all of the modern conveniences one would expect with a stay in Aspen.</p>
      <p>A stay at our lodge includes free continental breakfast in our dining room, daily maid service, free wireless internet access, and a fully-equipped conference facility. Guests are also invited to relax in one of our two outdoor hot tubs or in our lounge, where a 42-inch plasma TV and fireplace make for a pleasant area to unwind.</p>
      <p class="block-start">Located in the heart of downtown Aspen, the newly renovated Corwith Lodge possesses all the charms of a vintage European Ski Lodge, while offering all of the modern conveniences one would expect with a stay in Aspen.</p>
      <p class="block-follow">A stay at our lodge includes free continental breakfast in our dining room, daily maid service, free wireless internet access, and a fully-equipped conference facility. Guests are also invited to relax in one of our two outdoor hot tubs or in our lounge, where a 42-inch plasma TV and fireplace make for a pleasant area to unwind.</p>
    </section>

    <aside class="gallery">
      <h2>Our Gallery</h2>
      <div class="gallery-frame">
        <div class="thumb thumb-bed" role="img" aria-label="Guest room with canopy bed and patterned quilt"></div>
        <div class="thumb thumb-room" role="img" aria-label="Wood-panelled dining room with tables and chairs"></div>
        <div class="thumb thumb-room" role="img" aria-label="Lounge area with wooden furniture in warm light"></div>
        <div class="thumb thumb-bed" role="img" aria-label="Guest room with canopy bed and quilt"></div>
      </div>
    </aside>
  </main>

  <footer class="site-footer">© 2005 Corwith Lodge</footer>
  <a class="social-badge" href="#">
    <span class="mark"></span>
    <span class="label">Find us on:<br>Friendvia</span>
  </a>
</body>
</html>
```